Design a flyer for the 10th annual Velvet Pelican Putting Jubilee

We need a flyer for the web that is mini-golf themed and contains the following information:

Date: July 3rd
Location: Brindle Meadow Mini-Golf Course
4312 SE Brindle Meadow Lane, Portland OR
Time: 7pm
Entry Fee: $11.50/$10 prepaid

"featuring prizes"
OPTIONAL: previous winners (see below)
VePe Logo (attached)

Image size should be 600 pixels wide by 500 pixels high. (Fonts should be legible when used at smaller sizes.)

All this should be wrapped in a mini-golf theme. The concept of the tournament this year is "After Dark" so using blues, blacks, and other dark hues seems like a good idea, but open to interpretation!

For inspiration of previous flyers see:
http://velvetpelican.example/tidepool/files/2011/06/6thannualvpjubilee-big.gif

The name of the tournament will be:
Velvet Pelican Jubilee X: After Dark

Previous winners are:
2006 - Dean Falworth
2007 - Carl Pennington
2008 - Carl Pennington
2009 - tobin arquette
2010 - Neil Vandersloot
2011 - Gavin Thorley
2012 - Jules Corbett
2013 - Carl Pennington
2014 - tobin arquette

```html
<!DOCTYPE html>
<html lang="en">
<head>
<meta charset="utf-8">
<title>Velvet Pelican Jubilee X: After Dark</title>
<link rel="stylesheet" href="https://fonts.googleapis.com/css2?family=Montserrat:wght@800&family=Josefin+Sans:wght@700&family=Roboto+Condensed:ital,wght@0,400;1,400&family=Oswald:wght@500;600&family=Fredoka:wght@700&display=swap">
<style>
  :root {
    --bg: #5b3b8c;
    --white: #ffffff;
    --lavender: #efe8f7;
    --pink: #f0466e;
    --peak-hot: #ffb347;
    --peak-mid: #f2456c;
    --peak-cool: #7a3f9e;
  }
  html, body {
    margin: 0;
    padding: 0;
    overflow: hidden;
    background: var(--bg);
  }
  .flyer {
    position: relative;
    width: 1200px;
    height: 1000px;
    background: var(--bg);
    overflow: hidden;
    color: var(--white);
  }
  .flyer > * { position: absolute; margin: 0; }
  .course-terrain {
    left: 400px; top: 400px;
    width: 780px; height: 560px;
  }
  .event-series {
    left: 60px; top: 62px;
    font: 800 44px/1 "Montserrat", sans-serif;
    letter-spacing: 2px;
    text-transform: uppercase;
  }
  .event-theme {
    left: 52px; top: 112px;
    font: 700 150px/1 "Josefin Sans", sans-serif;
    letter-spacing: 12px;
    text-transform: uppercase;
  }
  .event-date {
    right: 58px; top: 262px;
    font: 800 66px/1 "Montserrat", sans-serif;
    letter-spacing: 2px;
    text-transform: uppercase;
  }
  .venue-name {
    left: 60px; top: 360px;
    font: italic 400 36px/1 "Roboto Condensed", sans-serif;
    text-transform: uppercase;
    color: var(--lavender);
  }
  .venue-address {
    left: 60px; top: 408px;
    font: italic 400 22px/1 "Roboto Condensed", sans-serif;
    color: var(--lavender);
  }
  .event-time {
    left: 60px; top: 458px;
    font: 600 58px/1 "Oswald", sans-serif;
    color: var(--pink);
  }
  .entry-fee {
    left: 168px; top: 466px;
    font: 500 28px/1.1 "Oswald", sans-serif;
    text-transform: uppercase;
    color: var(--pink);
  }
  .winners-heading {
    left: 60px; top: 628px;
    font: 800 26px/1.15 "Montserrat", sans-serif;
    text-transform: uppercase;
  }
  .winners-list {
    left: 60px; top: 698px;
    padding: 0;
    list-style: none;
    font: 400 22px/26px "Roboto Condensed", sans-serif;
  }
  .prizes-callout {
    left: 458px; top: 790px;
    font: 700 66px/0.95 "Fredoka", sans-serif;
    text-transform: uppercase;
    color: var(--white);
    text-shadow: 4px 4px 0 var(--pink), -2px -2px 0 var(--pink), 2px -2px 0 var(--pink), -2px 2px 0 var(--pink);
    transform: rotate(-8deg);
    transform-origin: left top;
  }
  .client-mark {
    left: 1000px; top: 860px;
    display: flex; align-items: center; gap: 12px;
    font: 800 40px/1 "Montserrat", sans-serif;
    color: var(--white);
  }
  .client-mark .dot {
    width: 22px; height: 22px;
    border-radius: 50%;
    background: var(--white);
  }
</style>
</head>
<body>
  <main class="flyer">
    <svg class="course-terrain" viewBox="0 0 780 560" role="img" aria-label="Glowing contour-line hill of a mini-golf green rising to a peak, with the hole cup near its base">
      <defs>
        <radialGradient id="terrainGlow" cx="0.5" cy="0.5" r="0.5" fx="0.52" fy="0.3">
          <stop offset="0" stop-color="var(--peak-hot)"/>
          <stop offset="0.3" stop-color="var(--peak-mid)"/>
          <stop offset="0.65" stop-color="var(--peak-cool)" stop-opacity="0.55"/>
          <stop offset="1" stop-color="var(--bg)" stop-opacity="0"/>
        </radialGradient>
      </defs>
      <ellipse cx="390" cy="280" rx="390" ry="280" fill="url(#terrainGlow)"/>
    </svg>

    <h2 class="event-series">Velvet Pelican Jubilee X:</h2>
    <h1 class="event-theme">After Dark</h1>
    <p class="event-date">July 3rd</p>

    <p class="venue-name">Brindle Meadow Mini-Golf Course</p>
    <p class="venue-address">4312 SE Brindle Meadow Lane, Portland OR</p>
    <p class="event-time">7PM</p>
    <p class="entry-fee">Entry fee:<br>$11.50/$10 prepaid</p>

    <h3 class="winners-heading">Previous<br>winners are:</h3>
    <ul class="winners-list">
      <li>2006 - Dean Falworth</li>
      <li>2007 - Carl Pennington</li>
      <li>2008 - Carl Pennington</li>
      <li>2009 - tobin arquette</li>
      <li>2010 - Neil Vandersloot</li>
      <li>2011 - Gavin Thorley</li>
      <li>2012 - Jules Corbett</li>
      <li>2013 - Carl Pennington</li>
      <li>2014 - tobin arquette</li>
    </ul>

    <p class="prizes-callout">Featuring<br>&nbsp;&nbsp;Prizes</p>

    <div class="client-mark"><span class="dot"></span>VePe</div>
  </main>
</body>
</html>
```